Shop Window Signs and Fence Designs

Hi guys im looking for creativity people in helping me with these designs 50 all up

Designs on various signage displays for shop windows and store fronts.

50 separate designs with on going work available.
Each design to be suppled in PDF

20 - Vertical designs - (posters)
20 - Horizontal designs - (banners) for hanging on fences e.g.
5 - Vertical - sales, garage sale EG
5 - Horizontal - sales, garage sale EG

MIX THINGS UP GUYS these are my samples below

At this stage only looking at straight eges designs.

COLOUR FULL DESIGNS EYE CATCHING
thanks guys lots more work to come for the right designer

Target Market(s)

Customers - Shoppers

Industry/Entity Type

Shop

Font styles to use
Serif
Sans Serif
Decorative
Script

Colors

Designer to choose colors to be used in the design.

Requirements
Must have
• POSTERS - in VERTICAL format
• 1900 x 1320 200gsm
• 2600 x 1600 200gsm
• 1540 x 1060 250gsm
• 2440 x1320 200gsm
• BANNERS - in HORIZONTAL format
• 1000 x 5000
• 1000 x 4000
• 1000 x 3000
• 1000 x 2000
Nice to have
• Be creative
Should not have
• Be creative

```html
<!DOCTYPE html>
<html lang="en">
<head>
<meta charset="utf-8">
<title>Sale – Up to 50% Off Storewide</title>
<link rel="stylesheet" href="https://fonts.googleapis.com/css2?family=Andika:wght@400;700&family=Original+Surfer&display=swap">
<style>
  :root {
    --page: #ffffff;
    --sign-red: #ff0019;
    --sign-ink: #ffffff;
  }
  * { margin: 0; padding: 0; box-sizing: border-box; }
  html, body {
    width: 1200px;
    height: 769px;
    overflow: hidden;
    background: var(--page);
  }
  .canvas {
    position: relative;
    width: 1200px;
    height: 769px;
    background: var(--page);
  }
  .sale-sign {
    position: absolute;
    left: 165px;
    top: 104px;
    width: 838px;
    height: 538px;
    background: var(--sign-red);
    color: var(--sign-ink);
    overflow: hidden;
  }
  .sale-sign > * { position: absolute; white-space: nowrap; line-height: 1; }

  .headline {
    left: 108px;
    top: 28px;
    width: 628px;
    display: flex;
    justify-content: space-between;
    font-family: "Original Surfer", fantasy;
    font-weight: 400;
    font-size: 96px;
    transform: scaleX(1.25);
    transform-origin: center top;
  }

  .offer-lead {
    left: 217px;
    top: 343px;
    transform-origin: left top;
    transform: rotate(-90deg);
    font-family: "Andika", sans-serif;
    font-size: 56px;
    letter-spacing: 1px;
  }
  .offer-amount {
    left: 280px;
    top: 136px;
    font-family: "Andika", sans-serif;
    font-size: 233px;
    letter-spacing: -6px;
  }
  .offer-percent {
    left: 533px;
    top: 163px;
    font-family: "Andika", sans-serif;
    font-size: 121px;
  }
  .offer-off {
    left: 535px;
    top: 295px;
    font-family: "Andika", sans-serif;
    font-size: 55px;
    letter-spacing: 1px;
  }

  .scope-store {
    left: 87px;
    top: 401px;
    font-family: "Andika", sans-serif;
    font-size: 85px;
    letter-spacing: -3px;
  }
  .scope-wide {
    left: 328px;
    top: 372px;
    width: 432px;
    height: 150px;
    overflow: visible;
  }
  .scope-wide text {
    font-family: "Original Surfer", fantasy;
    font-size: 172px;
    fill: var(--sign-ink);
  }
</style>
</head>
<body>
  <main class="canvas">
    <section class="sale-sign" aria-label="Sale sign">
      <h1 class="headline"><span>S</span><span>A</span><span>L</span><span>E</span></h1>
      <span class="offer-lead">UP TO</span>
      <span class="offer-amount">50</span>
      <span class="offer-percent">%</span>
      <span class="offer-off">OFF</span>
      <span class="scope-store">STORE</span>
      <svg class="scope-wide" viewBox="0 0 432 150" aria-label="WIDE">
        <text x="2" y="134" textLength="426" lengthAdjust="spacingAndGlyphs">WIDE</text>
      </svg>
    </section>
  </main>
</body>
</html>
```